Memento Mori Calendar

I’m looking for a graphic designer to create a Memento Mori–style life calendar that captures the essence of OLVENTRA — minimal, timeless, and deeply philosophical.

The design should be black and white only, with a refined, clean aesthetic and a sense of stillness and precision.
It should feel modern yet eternal, reflecting the themes of time, mortality, and presence.

Deliverables (Print-Ready Files):

24 x 30 in

24 x 32 in

24 x 36 in

A1 (594 x 841 mm)

All formats should be high-resolution and ready for professional printing (300 DPI, CMYK).

Design Requirements:

The calendar layout should follow the Memento Mori life calendar concept (weeks of life represented as small squares or circles).

The overall tone: minimal, meditative, monochrome.

Include the brand name: OLVENTRA (in an elegant, understated placement).

Add the following quote at the bottom or in a subtle position:

“Life can only be understood backwards; but it must be lived forwards.”
— Henrik Vastmoe

Target Market(s)

The OLVENTRA audience consists of urban, creative individuals aged 25 to 45, belonging to a middle to upper-middle income class. They lead conscious, quietly ambitious lives, seeking balance between inner depth and modern design. Their values center on awareness, presence, authenticity, and emotional depth, reflected in their preference for a monochrome, minimal, and timeless aesthetic. They tend to be introverted, reflective, and spiritually curious, drawn to brands that embody meaning and restraint rather than excess. Their cultural and stylistic affinities include Pyrel, Tulve, Ni Ostra, The Quiet Bench Guild, Durvanne, and Ombrix — labels that share OLVENTRAs devotion to simplicity, substance, and subtle ritual.

Font styles to use
Serif
Sans Serif

Colors

Designer to choose only greyscale colors for use in the design.

Requirements
Must have
• The calendar layout should follow the Memento Mori life calendar concept (weeks of life represented as small squares or circles). The overall tone: minimal, meditative, monochrome. Include the brand name: qrnvalto (in an elegant, understated placement). Add the following quote at the bottom or in a subtle position: “Life can only be understood backwards; but it must be lived forwards.” — Henrik Vastmoe

```html
<!DOCTYPE html>
<html lang="en">
<head>
<meta charset="utf-8">
<title>OLVENTRA — Memento Mori Life Calendar</title>
<link rel="stylesheet" href="https://fonts.googleapis.com/css2?family=Inter+Tight:ital,wght@0,400;0,700;0,800;1,300;1,400;1,800&display=swap">
<style>
  :root {
    --backdrop: #f0f0f0;
    --paper: #ffffff;
    --ink: #0b0b0b;
    --ink-soft: #222222;
  }
  * { box-sizing: border-box; margin: 0; padding: 0; }
  html, body {
    width: 1018px;
    height: 1200px;
    overflow: hidden;
    background: var(--backdrop);
  }
  body {
    display: flex;
    justify-content: center;
    font-family: "Inter Tight", "Helvetica Neue", Arial, sans-serif;
    color: var(--ink);
  }
  .poster {
    position: relative;
    width: 842px;
    height: 1200px;
    background: var(--paper);
    overflow: hidden;
  }
  .brand-mark {
    position: absolute;
    left: 40px;
    top: 29px;
    font-size: 12px;
    font-weight: 400;
    letter-spacing: 0.72em;
    line-height: 14px;
  }
  .title {
    position: absolute;
    left: 37px;
    top: 46px;
    font-size: 75px;
    font-weight: 800;
    line-height: 63px;
    letter-spacing: -0.045em;
  }
  .quote {
    position: absolute;
    right: 30px;
    top: 72px;
    text-align: right;
    font-style: italic;
    font-weight: 300;
    font-size: 13px;
    line-height: 16.5px;
    color: var(--ink-soft);
  }
  .quote-mark {
    font-style: italic;
    font-weight: 800;
    font-size: 30px;
    line-height: 0;
    vertical-align: -8px;
    margin-right: 8px;
    color: var(--ink);
  }
  .quote-author {
    display: block;
    margin-top: 10px;
    font-size: 11.5px;
    letter-spacing: 0.18em;
  }
  .life-grid {
    position: absolute;
    left: 40px;
    top: 211px;
    width: 759px;
    display: flex;
    flex-direction: column;
    gap: 25px;
  }
  .decade { height: 92px; }
  .decade-label {
    font-size: 17px;
    font-weight: 700;
    letter-spacing: -0.03em;
    line-height: 20px;
    border-bottom: 2px solid var(--ink);
    padding-bottom: 1px;
  }
  .week-field {
    display: block;
    margin-top: 6px;
    width: 759px;
    height: 63px;
  }
  .footer-brand {
    position: absolute;
    left: 40px;
    top: 1146px;
    display: flex;
    align-items: center;
    gap: 9px;
    font-size: 12px;
    font-weight: 700;
    letter-spacing: 0.08em;
  }
  .footer-brand-square {
    width: 31px;
    height: 31px;
    background: var(--ink);
  }
  .legend {
    position: absolute;
    right: 41px;
    top: 1153px;
    display: flex;
    align-items: center;
    gap: 5px;
    font-size: 13px;
    font-weight: 700;
    letter-spacing: -0.02em;
  }
  .legend-box {
    width: 11px;
    height: 11px;
    border: 1px solid var(--ink);
  }
  .pattern-defs { position: absolute; width: 0; height: 0; }
</style>
</head>
<body>
  <svg class="pattern-defs" aria-hidden="true">
    <defs>
      <pattern id="week-cell" width="10.1" height="9" patternUnits="userSpaceOnUse">
        <rect x="0.5" y="0.5" width="7.6" height="6.6" fill="none" stroke="#111" stroke-width="0.8"/>
      </pattern>
    </defs>
  </svg>

  <main class="poster">
    <p class="brand-mark">OLVENTRA</p>
    <h1 class="title">Memento<br>Mori</h1>

    <blockquote class="quote">
      <span class="quote-mark">“</span>Life can only be understood backwards;<br>
      but it must be lived forwards.”
      <cite class="quote-author">— Henrik Vastmoe</cite>
    </blockquote>

    <section class="life-grid">
      <div class="decade">
        <h2 class="decade-label">Birth - 10 years</h2>
        <svg class="week-field" viewBox="0 0 759 63" aria-label="520 weeks">
          <rect width="757.5" height="45" fill="url(#week-cell)"/>
          <rect y="45" width="747.4" height="9" fill="url(#week-cell)"/>
          <rect y="54" width="737.3" height="9" fill="url(#week-cell)"/>
        </svg>
      </div>
      <div class="decade">
        <h2 class="decade-label">11 - 20 years</h2>
        <svg class="week-field" viewBox="0 0 759 63" aria-label="520 weeks">
          <rect width="757.5" height="45" fill="url(#week-cell)"/>
          <rect y="45" width="747.4" height="9" fill="url(#week-cell)"/>
          <rect y="54" width="737.3" height="9" fill="url(#week-cell)"/>
        </svg>
      </div>
      <div class="decade">
        <h2 class="decade-label">21 - 30 years</h2>
        <svg class="week-field" viewBox="0 0 759 63" aria-label="520 weeks">
          <rect width="757.5" height="45" fill="url(#week-cell)"/>
          <rect y="45" width="747.4" height="9" fill="url(#week-cell)"/>
          <rect y="54" width="737.3" height="9" fill="url(#week-cell)"/>
        </svg>
      </div>
      <div class="decade">
        <h2 class="decade-label">31 - 40 years</h2>
        <svg class="week-field" viewBox="0 0 759 63" aria-label="520 weeks">
          <rect width="757.5" height="45" fill="url(#week-cell)"/>
          <rect y="45" width="747.4" height="9" fill="url(#week-cell)"/>
          <rect y="54" width="737.3" height="9" fill="url(#week-cell)"/>
        </svg>
      </div>
      <div class="decade">
        <h2 class="decade-label">41 - 50 years</h2>
        <svg class="week-field" viewBox="0 0 759 63" aria-label="520 weeks">
          <rect width="757.5" height="45" fill="url(#week-cell)"/>
          <rect y="45" width="747.4" height="9" fill="url(#week-cell)"/>
          <rect y="54" width="737.3" height="9" fill="url(#week-cell)"/>
        </svg>
      </div>
      <div class="decade">
        <h2 class="decade-label">51 - 60 years</h2>
        <svg class="week-field" viewBox="0 0 759 63" aria-label="520 weeks">
          <rect width="757.5" height="45" fill="url(#week-cell)"/>
          <rect y="45" width="747.4" height="9" fill="url(#week-cell)"/>
          <rect y="54" width="737.3" height="9" fill="url(#week-cell)"/>
        </svg>
      </div>
      <div class="decade">
        <h2 class="decade-label">61 - 70 years</h2>
        <svg class="week-field" viewBox="0 0 759 63" aria-label="520 weeks">
          <rect width="757.5" height="45" fill="url(#week-cell)"/>
          <rect y="45" width="747.4" height="9" fill="url(#week-cell)"/>
          <rect y="54" width="737.3" height="9" fill="url(#week-cell)"/>
        </svg>
      </div>
      <div class="decade">
        <h2 class="decade-label">71 - 80 years</h2>
        <svg class="week-field" viewBox="0 0 759 63" aria-label="520 weeks">
          <rect width="757.5" height="45" fill="url(#week-cell)"/>
          <rect y="45" width="747.4" height="9" fill="url(#week-cell)"/>
          <rect y="54" width="737.3" height="9" fill="url(#week-cell)"/>
        </svg>
      </div>
    </section>

    <footer>
      <div class="footer-brand"><span class="footer-brand-square"></span>OLVENTRA</div>
      <div class="legend"><span class="legend-box"></span>= 1 week</div>
    </footer>
  </main>
</body>
</html>
```